Business Card Design for LeafCrest (Farming Devices)

We need Business Cards for our new Company based in Switzerland called "LeafCrest" We develop innovativ products for indoor and outdoor Farming for household and components for vertical farming. Our initial BloomNest gives people the possibility to grow their own food at home all year round. The design should communicate freshness, innovation, health.

```html
<!DOCTYPE html>
<html lang="en">
<head>
<meta charset="utf-8">
<title>LeafCrest Business Card</title>
<link rel="stylesheet" href="https://fonts.googleapis.com/css2?family=Lato:ital,wght@0,400;0,700;0,900;1,700&family=Open+Sans:wght@400&display=swap">
<style>
  :root {
    --backdrop: #d2d2d2;
    --paper: #ffffff;
    --ink: #1e1e1e;
    --night: #000000;
    --brand-blue: #0a6fbe;
    --brand-green: #6ab23e;
    --mist: #d9d7dc;
  }
  * { margin: 0; padding: 0; box-sizing: border-box; }
  html, body {
    width: 1200px; height: 1177px; overflow: hidden;
    background: var(--backdrop);
  }
  .card {
    position: absolute; left: 280px;
    width: 646px; height: 387px; overflow: hidden;
  }
  .card-front { top: 175px; background: var(--paper); }
  .card-back { top: 616px; background: var(--night); }
  .card-art { position: absolute; inset: 0; width: 100%; height: 100%; }

  .holder { position: absolute; left: 27px; top: 80px; font-family: "Lato", sans-serif; }
  .holder-name { font-weight: 900; font-size: 34px; letter-spacing: 0.3px; line-height: 1; }
  .holder-name .first { color: var(--brand-blue); }
  .holder-name .last { color: var(--brand-green); }
  .holder-role { margin-top: 4px; font-weight: 700; font-style: italic; font-size: 21px; color: var(--ink); }

  .contacts { position: absolute; left: 381px; top: 54px; list-style: none; font-family: "Open Sans", sans-serif; font-size: 18.5px; color: var(--ink); }
  .contacts li { display: flex; align-items: flex-start; height: 38.5px; line-height: 28px; }
  .contacts li.address { line-height: 23px; padding-top: 2px; }
  .contacts .icon { width: 28px; height: 28px; margin-right: 10px; flex: none; }
  .contacts li.address .icon { margin-top: -2px; }

  .front-brand { position: absolute; left: 30px; bottom: 14px; font-family: "Lato", sans-serif; font-weight: 700; font-size: 37px; color: var(--paper); }
  .back-brand { position: absolute; left: 0; right: 0; top: 168px; text-align: center; font-family: "Lato", sans-serif; font-weight: 700; font-size: 88px; color: var(--brand-green); line-height: 1; }
</style>
</head>
<body>
  <section class="card card-front" aria-label="Card front">
    <svg class="card-art" viewBox="0 0 646 387" aria-hidden="true">
      <defs>
        <linearGradient id="swoosh-fill" x1="0" y1="0" x2="1" y2="0">
          <stop offset="0" stop-color="#1a7bbd"/>
          <stop offset="0.3" stop-color="#3f9a78"/>
          <stop offset="0.65" stop-color="var(--brand-green)"/>
        </linearGradient>
      </defs>
      <path d="M0,236 Q390,238 545,387 L0,387 Z" fill="var(--mist)"/>
      <path d="M0,248 Q330,246 390,330 Q402,358 378,387 L0,387 Z" fill="url(#swoosh-fill)"/>
    </svg>

    <div class="holder">
      <div class="holder-name"><span class="first">NAME</span> <span class="last">SURNAME</span></div>
      <div class="holder-role">Position</div>
    </div>

    <ul class="contacts">
      <li>
        <svg class="icon" viewBox="0 0 28 28" aria-hidden="true"><circle cx="14" cy="14" r="14" fill="var(--brand-blue)"/><path d="M10 8c-1 0-2 1-2 2 0 6 4 10 10 10 1 0 2-1 2-2l-3-2-2 1c-2-1-3-2-4-4l1-2-2-3z" fill="none" stroke="#fff" stroke-width="1.5"/></svg>
        0812 555 014 7
      </li>
      <li>
        <svg class="icon" viewBox="0 0 28 28" aria-hidden="true"><circle cx="14" cy="14" r="14" fill="var(--brand-blue)"/><rect x="10" y="8" width="8" height="4" fill="#fff"/><rect x="8" y="12" width="12" height="6" rx="1" fill="#fff"/><rect x="10" y="16" width="8" height="4" fill="#fff" stroke="var(--brand-blue)" stroke-width="1"/></svg>
        0812 555 014 7
      </li>
      <li>
        <svg class="icon" viewBox="0 0 28 28" aria-hidden="true"><circle cx="14" cy="14" r="14" fill="var(--brand-blue)"/><rect x="8" y="9.5" width="12" height="9" fill="none" stroke="#fff" stroke-width="1.5"/><path d="M8 10l6 5 6-5" fill="none" stroke="#fff" stroke-width="1.5"/></svg>
        email@leafcrest.com
      </li>
      <li class="address">
        <svg class="icon" viewBox="0 0 28 28" aria-hidden="true"><circle cx="14" cy="14" r="14" fill="var(--brand-blue)"/><path d="M14 21s-5-5-5-9a5 5 0 0 1 10 0c0 4-5 9-5 9z" fill="#fff"/><circle cx="14" cy="12" r="2" fill="var(--brand-blue)"/></svg>
        <span>address 1<br>city, country, zip</span>
      </li>
    </ul>

    <div class="front-brand">LeafCrest</div>
  </section>

  <section class="card card-back" aria-label="Card back">
    <svg class="card-art" viewBox="0 0 646 387" aria-hidden="true">
      <path d="M0,350 Q300,270 646,340 L646,387 L0,387 Z" fill="var(--brand-green)"/>
      <path d="M0,372 Q330,300 646,346 L646,387 L0,387 Z" fill="#4e9a66" opacity="0.9"/>
      <path d="M0,387 L0,380 Q330,318 646,352 L646,387 Z" fill="var(--brand-blue)"/>
    </svg>
    <div class="back-brand">LeafCrest</div>
  </section>
</body>
</html>
```